Webdesign for Brisvane for use on webpage

We aim to deliver insights for power consumers in the nordic market in the B2B market, without being a supplier.

Since we are helping customers in the green transition and reducing CO2 emissions, green colors would be preferred, but we are keeping an open mind. We would like to communicate transperancy, awareness and enabling economic potential for customers.

We deliver our product on a SaaS platform through visualization in dashboards

Target Market(s)

B2B

Industry/Entity Type

Power Consumption

Number of Pages Required

1 page

Colors
0054AA
0677BA
7BADD7
CADEEF
E8F1F8
0094D4
00A9DD
6FCCEA
C7EBF8
E9F6FB
00AB8E
00BBA5
67D7C9
C6EFE9
E9F9F6
59FF00
82FF00
B8FF75
E3FFCB
F4FFEA

Requirements
Must have
• The general looks and color schemes must be in line with logo called "brisvane.eps" - see attached

```html
<!DOCTYPE html>
<html lang="en">
<head>
<meta charset="utf-8">
<title>Brisvane – Energy Data Insights</title>
<link rel="stylesheet" href="https://fonts.googleapis.com/css2?family=Montserrat:wght@500;600;700;800&family=Arimo:wght@400&display=swap">
<style>
:root{
  --navy:#123f96;
  --green:#6cb52f;
  --green-light:#7cc23b;
  --ink:#333a45;
  --muted:#5b6270;
  --rule:#e3e6ea;
  --white:#ffffff;
}
*{box-sizing:border-box;margin:0;padding:0}
html,body{width:1200px;height:3664px;overflow:hidden;background:var(--white)}
body{position:relative;font-family:"Arimo",Arial,sans-serif;color:var(--ink)}
.abs{position:absolute}
.head-font{font-family:"Montserrat",Arial,sans-serif}

/* header */
.site-header{position:absolute;left:0;top:0;width:1200px;height:136px;background:var(--white);z-index:3}
.brand-badge{position:absolute;left:108px;top:0;width:206px;height:214px;border-radius:0 0 103px 103px;background:var(--white);z-index:4;display:flex;align-items:flex-end;justify-content:center;padding-bottom:52px}
.brand-name{font-family:"Montserrat",Arial,sans-serif;font-weight:800;font-size:31px;color:var(--navy);letter-spacing:.5px;white-space:nowrap}
.main-nav{position:absolute;top:61px;left:580px;font-family:"Montserrat",Arial,sans-serif;font-weight:600;font-size:14px;color:#1f2a3a}
.main-nav a{color:inherit;text-decoration:none;position:absolute;white-space:nowrap}
.main-nav a.active{color:var(--navy)}

/* hero */
.hero{position:absolute;left:0;top:136px;width:1200px;height:754px;overflow:hidden}
.hero-photo{position:absolute;inset:0;background:
  radial-gradient(circle at 800px 360px,#f5c76a 0,#c7862f 90px,rgba(90,90,40,0) 260px),
  radial-gradient(ellipse at 300px 200px,#4c6a2e 0,#2a3a1a 420px),
  linear-gradient(180deg,#3f5a27 0,#2e3b1c 55%,#4a3422 80%,#3a2818 100%)}
.hero-title{left:151px;top:352px;font-size:60px;font-weight:700;color:var(--white);letter-spacing:1px;line-height:72px}
.hero-sub{left:151px;top:430px;font-size:38px;font-weight:600;color:var(--white);line-height:46px}
.hero-text{left:155px;top:491px;width:480px;font-size:14px;line-height:26px;color:var(--white)}
.btn{display:flex;align-items:center;justify-content:center;border-radius:30px;font-family:"Montserrat",Arial,sans-serif;font-weight:600;font-size:15px;color:var(--white);text-decoration:none;white-space:nowrap}
.btn-green{background:var(--green)}
.btn-navy{background:var(--navy)}
.btn-outline{border:2px solid var(--white)}

/* section titles */
.section-title{font-family:"Montserrat",Arial,sans-serif;font-weight:600;font-size:32px;color:var(--navy);line-height:40px}
.section-title span{color:var(--green)}
.title-rule{height:3px;background:var(--navy)}

/* welcome */
.welcome-text{left:111px;top:1084px;width:477px;font-size:13.5px;line-height:25.7px;color:#3c4350;text-align:justify}
.welcome-mark{left:667px;top:994px;width:394px;height:394px;border:9px solid var(--navy);border-radius:50%;display:flex;align-items:center;justify-content:center}
.welcome-mark .brand-name{font-size:44px}

/* services */
.service-card{top:1574px;width:315px;height:383px;border-radius:6px;color:var(--white);text-align:center}
.service-card.navy{background:var(--navy)}
.service-card.green{background:var(--green-light)}
.service-card svg{position:absolute;left:107px;top:42px}
.service-card h3{position:absolute;left:0;right:0;top:148px;font-family:"Montserrat",Arial,sans-serif;font-weight:600;font-size:20px;line-height:26px}
.service-card h4{position:absolute;left:0;right:0;top:178px;font-family:"Montserrat",Arial,sans-serif;font-weight:600;font-size:14px;letter-spacing:.3px;line-height:18px}
.service-card p{position:absolute;left:24px;right:24px;top:212px;font-size:14px;line-height:24px}
.service-card .btn{position:absolute;left:85px;top:304px;width:144px;height:48px;font-size:15px}

/* feature band */
.feature-band{left:0;top:2036px;width:1200px;height:531px;background:linear-gradient(90deg,#0a1a3a 0,#0d2456 45%,#0b1f4c 100%)}
.feature-art{left:0;top:2036px;width:540px;height:531px;background:radial-gradient(circle at 290px 260px,#c9d8ff 0,#4d7ee0 60px,#173f9c 170px,rgba(10,26,58,0) 300px)}
.feature-title{left:586px;top:2136px;font-size:32px;font-weight:600;color:var(--white);line-height:40px}
.feature-sub{left:586px;top:2186px;font-size:21px;font-weight:500;color:var(--white);letter-spacing:.5px;line-height:26px}
.feature-text{left:588px;top:2241px;width:502px;font-size:13.5px;line-height:25.7px;color:#e4eaf7;text-align:justify}

/* blog */
.blog-photo{top:2695px;width:313px;height:277px}
.blog-box{top:2915px;width:287px;height:218px;background:var(--white);box-shadow:0 2px 10px rgba(0,0,0,.12);text-align:center}
.blog-box .date{position:absolute;left:0;right:0;top:26px;font-family:"Montserrat",Arial,sans-serif;font-weight:500;font-size:20px;color:var(--navy)}
.blog-box h3{position:absolute;left:14px;right:14px;top:63px;font-family:"Montserrat",Arial,sans-serif;font-weight:500;font-size:18.5px;line-height:27px;color:#2b3240}
.blog-box p{position:absolute;left:18px;right:18px;top:124px;font-size:13px;line-height:24px;color:var(--muted)}

/* footer */
.footer-heading{font-family:"Montserrat",Arial,sans-serif;font-weight:500;font-size:21px;color:var(--white)}
.footer-item{font-family:"Montserrat",Arial,sans-serif;font-size:15px;line-height:22px;color:var(--white);letter-spacing:.3px}
.footer-mark{left:149px;top:3306px;width:260px;display:flex;flex-direction:column;align-items:center;gap:18px}
.footer-mark .ring{width:150px;height:150px;border:5px solid var(--white);border-radius:50%}
.footer-mark .brand-name{color:var(--white);font-size:46px}
.newsletter-input{left:765px;top:3423px;width:324px;height:42px;background:var(--white);border-radius:2px;padding-left:18px;display:flex;align-items:center;font-size:14px;color:#555}
</style>
</head>
<body>

<header class="site-header">
  <nav class="main-nav">
    <a class="active" style="left:0">HOME</a>
    <a style="left:90px">ABOUT US</a>
    <a style="left:211px">SERVICES</a>
    <a style="left:326px">NEWS</a>
    <a style="left:416px">CONTACT US</a>
  </nav>
</header>
<div class="brand-badge"><span class="brand-name">BRISVANE</span></div>

<section class="hero">
  <div class="hero-photo" role="img" aria-label="Glowing light bulb standing in soil beside a young green sprout"></div>
  <svg class="abs" style="left:0;top:0" width="1200" height="754" viewBox="0 0 1200 754">
    <path d="M0 650 Q600 818 1200 650 L1200 754 L0 754 Z" fill="var(--green)"/>
    <path d="M0 654 Q600 856 1200 654 L1200 754 L0 754 Z" fill="#ffffff"/>
  </svg>
</section>
<div class="abs head-font hero-title">BRISVANE</div>
<div class="abs head-font hero-sub">ENERGY DATA INSIGHTS</div>
<p class="abs hero-text">Sed ut perspiciatis unde omnis iste natus error sit voluptatem accusantium doloremque laudantium, totam</p>
<a class="abs btn btn-green" style="left:155px;top:563px;width:164px;height:56px">READ MORE</a>

<h2 class="abs section-title" style="left:111px;top:1003px">WELCOME TO <span>BRISVANE</span></h2>
<div class="abs title-rule" style="left:111px;top:1060px;width:60px"></div>
<p class="abs welcome-text">Sed ut perspiciatis unde omnis iste natus error sit voluptatem accusantium dolo rem que laudantium, totam rem aperiam, eaque ipsa quae ab illo inventore veritatis et quasi architecto beatae vitae dicta sunt explicabo. Nemo enim ipsam voluptatem quia voluptas sit aspernatur aut odit aut fugit, sed quia consequuntur magni dolores eos qui ratione voluptatem sequi nesciunt. Neque porro quisquam est, qui dolorem ipsum quia dolor sit amet, consectetur, adipisci ut labore et dolore magnam aliquam quaerat voluptatem.Ut enim ad minima laboriosam, nisi ut aliquid ex ea commodi consequatur</p>
<a class="abs btn btn-navy" style="left:111px;top:1325px;width:148px;height:56px">READ MORE</a>
<div class="abs welcome-mark"><span class="brand-name">BRISVANE</span></div>

<div class="abs" style="left:111px;top:1443px;width:978px;height:1px;background:var(--rule)"></div>

<h2 class="abs section-title" style="left:0;width:1200px;text-align:center;top:1481px">OUR <span>SERVICES</span></h2>
<div class="abs title-rule" style="left:570px;top:1533px;width:60px"></div>

<div class="abs service-card navy" style="left:111px">
  <svg width="100" height="80" viewBox="0 0 100 80" fill="none" stroke="#fff" stroke-width="3" stroke-linejoin="round">
    <path d="M6 30h40v26H22l-10 10v-10H6z"/>
    <path d="M42 8h52v32H80l-8 10v-10H42z"/>
    <circle cx="55" cy="24" r="4"/><circle cx="68" cy="24" r="4"/><circle cx="81" cy="24" r="4"/>
  </svg>
  <h3>COMMUNICATE</h3><h4>TRANSPARENCY</h4>
  <p>Sed ut perspiciatis unde omnis iste natus error sit voluptatem accusa ntium doloremque laudantium</p>
  <a class="btn btn-outline">READ MORE</a>
</div>
<div class="abs service-card green" style="left:443px">
  <svg width="100" height="100" viewBox="0 0 100 100" fill="none" stroke="#fff" stroke-width="3" stroke-linejoin="round" stroke-linecap="round">
    <path d="M30 90V72c-8-6-12-14-10-24 3-14 15-20 28-18 14 2 22 14 20 27-1 8-6 13-12 16v17"/>
    <path d="M50 62V42M42 50l8-9 8 9"/>
    <path d="M50 24V8M45 13l5-5 5 5M20 30 10 22M84 24l-10 8M8 50h10M82 50h10"/>
  </svg>
  <h3>AWARENESS</h3>
  <p>Sed ut perspiciatis unde omnis iste natus error sit voluptatem accusa ntium doloremque laudantium</p>
  <a class="btn btn-outline">READ MORE</a>
</div>
<div class="abs service-card navy" style="left:775px">
  <svg width="100" height="80" viewBox="0 0 100 80" fill="none" stroke="#fff" stroke-width="3" stroke-linejoin="round" stroke-linecap="round">
    <path d="M10 78h84"/>
    <rect x="18" y="56" width="14" height="22"/><rect x="42" y="42" width="14" height="36"/><rect x="66" y="26" width="14" height="52"/>
    <path d="M14 46 58 8M46 8h12v12"/>
  </svg>
  <h3>ECONOMIC</h3><h4>POTENTIAL</h4>
  <p>Sed ut perspiciatis unde omnis iste natus error sit voluptatem accusa ntium doloremque laudantium</p>
  <a class="btn btn-outline">READ MORE</a>
</div>

<section class="abs feature-band"></section>
<div class="abs feature-art" role="img" aria-label="Digital light bulb held above a wireframe hand, ringed by energy icons"></div>
<h2 class="abs head-font feature-title">SED UT PERSPICIATIS</h2>
<div class="abs head-font feature-sub">OMNIS ISTE NATUS ERROR SIT VOLUPTATEM</div>
<p class="abs feature-text">Nemo enim ipsam voluptatem quia voluptas sit aspernatur aut odit aut fugit, sed quia consequuntur magni dolores eos qui ratione voluptatem sequi nesciunt. Neque porro quisquam est, qui dolorem ipsum quia dolor sit amet, consectetur, adipisci velit, sed quia non numquam eius modi tempora incidunt ut labore et dolore magnam aliquam quaerat voluptatem.</p>
<a class="abs btn btn-green" style="left:586px;top:2394px;width:154px;height:56px;font-size:16px">READ MORE</a>

<h2 class="abs section-title" style="left:0;width:1200px;text-align:center;top:2615px">LATEST <span>BLOG</span></h2>
<div class="abs title-rule" style="left:570px;top:2667px;width:60px"></div>

<div class="abs blog-photo" style="left:112px;background:linear-gradient(135deg,#7c8fa6,#c9b59a 55%,#5b6b3a)" role="img" aria-label="Hand holding a glowing bulb beside coin stacks and a small tree"></div>
<div class="abs blog-photo" style="left:445px;background:linear-gradient(180deg,#7fa4c6,#e6c48c 45%,#6f6a45 75%,#4d4a30)" role="img" aria-label="Wind turbines on hills at sunrise"></div>
<div class="abs blog-photo" style="left:776px;background:linear-gradient(160deg,#2f5f8c,#6fa6c9 50%,#2b4e6c)" role="img" aria-label="Wind turbines under a sky with connected network icons"></div>

<div class="abs blog-box" style="left:128px"><div class="date">08 AUG 2021</div><h3>Sed ut perspiciatis unde omnis iste natus</h3><p>Nemo enim ipsam voluptatem quia voluptas sit aspernatur aut odit aut fugit, eos qui ratione voluptatem</p></div>
<div class="abs blog-box" style="left:461px"><div class="date">08 AUG 2021</div><h3>Sed ut perspiciatis unde omnis iste natus</h3><p>Nemo enim ipsam voluptatem quia voluptas sit aspernatur aut odit aut fugit, eos qui ratione voluptatem</p></div>
<div class="abs blog-box" style="left:793px"><div class="date">08 AUG 2021</div><h3>Sed ut perspiciatis unde omnis iste natus</h3><p>Nemo enim ipsam voluptatem quia voluptas sit aspernatur aut odit aut fugit, eos qui ratione voluptatem</p></div>

<footer>
  <svg class="abs" style="left:0;top:3190px" width="1200" height="474" viewBox="0 0 1200 474">
    <path d="M0 72 Q600 -70 1200 72 L1200 474 L0 474 Z" fill="var(--green)"/>
    <path d="M0 80 Q600 -55 1200 80 L1200 474 L0 474 Z" fill="var(--navy)"/>
  </svg>
  <div class="abs footer-mark"><div class="ring"></div><span class="brand-name">BRISVANE</span></div>

  <h3 class="abs footer-heading" style="left:488px;top:3302px">CONTACT US</h3>
  <svg class="abs" style="left:489px;top:3364px" width="18" height="24" viewBox="0 0 18 24" fill="none" stroke="#fff" stroke-width="1.6"><path d="M9 23s8-8 8-14A8 8 0 0 0 1 9c0 6 8 14 8 14z"/><circle cx="9" cy="9" r="3"/></svg>
  <div class="abs footer-item" style="left:528px;top:3357px;width:190px">Address<br>14 Lorem Harbour Way</div>
  <svg class="abs" style="left:488px;top:3447px" width="22" height="20" viewBox="0 0 24 24" fill="none" stroke="#fff" stroke-width="1.6"><path d="M5 2h4l2 5-3 2a12 12 0 0 0 7 7l2-3 5 2v4a2 2 0 0 1-2 2A19 19 0 0 1 3 4a2 2 0 0 1 2-2z"/></svg>
  <div class="abs footer-item" style="left:528px;top:3443px">Phone :<br>000-555-0184</div>
  <svg class="abs" style="left:488px;top:3516px" width="22" height="16" viewBox="0 0 22 16" fill="none" stroke="#fff" stroke-width="1.6"><rect x="1" y="1" width="20" height="14"/><path d="M1 1l10 8 10-8"/></svg>
  <div class="abs footer-item" style="left:528px;top:3511px">Email :<br>hello@brisvane-mail.com</div>

  <h3 class="abs footer-heading" style="left:765px;top:3299px">NEWSLETTER</h3>
  <p class="abs" style="left:765px;top:3350px;width:330px;font-size:13.5px;line-height:25px;color:#fff">Sed ut perspiciatis unde omnis iste natus error sit voluptatem accusantium doloremque</p>
  <div class="abs newsletter-input">Enter Email</div>
  <a class="abs btn btn-green" style="left:765px;top:3482px;width:136px;height:42px;border-radius:2px;font-weight:500">SUBSCRIBE</a>

  <p class="abs" style="left:0;width:1200px;top:3621px;text-align:center;font-size:14.5px;color:#fff">© Copyright 2021.All Rights Reserved</p>
</footer>

</body>
</html>
```